Vacation/Holiday Home Wordpress Website

I currently have a website for our vacation/holiday rental home. It is 6 years old and needs a complete redesign to acommodate many new features available today. The existing website can be seen at www.coralwindstays.co.uk . The purpose of the website is mainly to provide useful infomation about our home, the destination of Barbados. The customer is also able to check availability and book. Please note that there is a booking element to the website which is hosted externally. This can be seen at

http://stay.reservequick-hub.net/PickArrival_Mini.asp?ref=kTR%3DWQPA%26LMN%3DHXJX

I now wish to add key functionality such as:

- Video of property and area
- Customer video testimonials
- Other useful information

The navigation, menus and buttons need to be re designed to give a modern, innovative and professional look and feel.

My customers are mainly females between the ages of 35 and 55. The website needs to reassure customers who are parting with a lot of mony by booking online. It needs to give a sense of trust as this may be a once in a lifetime trip which they have saved up for for a long time. Many visitors to the website will be referred by other websites such as www.nestroam.co.uk and www.villaquarters.co.uk.
Updates

Dear designers, 

Thank you for taking the time to write some further comments to you all. 

1. The homepage should have an availability search function as a key feature

2. The look and feel does NOT need to have the 3 feature columns like my current website has

3.  There should not be too much text on the homepage. Brief text can be included with 'more'  buttons to reveal more information 

4.  For designs that are under consideration, we will need to see a design for the other pages as they will be different to the homepage. Information from other pages on the existing website can be used. 

Reason: Dear all, I will be providing extensive feedback later today following a review that we have conducted with a group of our guests. To enable you to read and use this information, we have extended the deadline by 5 days. Thank you for the design submisions so far. We hope that the additional feedback will enable you to amend your designs appropriately. Regards Martin Elswick

Dear all,

Thank you for your designs.  I apologise that I am unable to give detailed feedback on each and every design submitted.  I will contact you individually and indicate whether we would like you to submit any further designs.  These should take into account the feedback below.

Feedback from design review group

1.  Logo should not be displayed in a white box.  It should blend in with the background or be overlayed onto the picture.

2.  There must be an availability calendar on the home page.

3.  Any background image should be subtle, maybe blurred and not distract from the main area.

4.  Text should be limited to a few key words with a 'read more' button to reveal more information.

5.  A gallery/slide show should be featured in the top part of the screen

6.  Icons can be used as navigation buttons

7.  Video testimonials is a key feature and should appear on the home page

8.   The use of bold and vibrant colours is preferred

9.   The 3 column format of the old website should not be copied

Regards

Martin

Target Market(s)

Female's, Families, 35 to 55 year olds, travellers to Barbados

Industry/Entity Type

Online

Requirements
Must have
• Pictures
Video
Testimonials
Clear and stylish navigation
Easy to use navigation
Should not have
• Dated look or feel

```html
<!DOCTYPE html>
<html lang="en">
<head>
<meta charset="utf-8">
<title>Coral Wind Stays – Holiday Home</title>
<link rel="stylesheet" href="https://fonts.googleapis.com/css2?family=Mulish:wght@300;400;600;700&family=Open+Sans:wght@400;700&display=swap">
<style>
:root{
  --yellow:#f5c518;
  --yellow-light:#f8d624;
  --yellow-deep:#efa80b;
  --amber:#eca80e;
  --red:#e8251f;
  --blue:#5bb8ea;
  --card-grey:#e4d9d7;
  --pale:#f8dd8c;
  --white:#ffffff;
  --dark:#24221c;
  --text:#2b2b2b;
  --line:#dcdcdc;
}
*{box-sizing:border-box;margin:0;padding:0}
html,body{width:1200px;height:2996px;overflow:hidden}
body{position:relative;background:var(--white);font-family:"Mulish",sans-serif;color:var(--text)}
.abs{position:absolute}
.top-rule{left:0;top:0;width:1200px;height:6px;background:var(--yellow)}

/* header */
.brand{left:110px;top:44px;display:flex;align-items:center;gap:14px}
.brand-dot{width:34px;height:34px;border-radius:50%;background:var(--red)}
.brand-name{font-family:"Mulish",sans-serif;font-weight:600;font-size:26px;letter-spacing:3px;color:var(--red)}
.main-nav{left:594px;top:50px;display:flex;gap:12px;align-items:center}
.nav-pill{height:44px;padding:0 22px;border-radius:22px;background:var(--amber);color:var(--white);font-weight:700;font-size:16px;line-height:44px}
.social{width:44px;height:44px;border-radius:50%;background:var(--amber);margin-left:2px}

/* hero */
.hero{left:0;top:140px;width:1200px;height:440px;background:linear-gradient(180deg,#3e86d4 0%,#8fc3ee 30%,#4fd6cf 48%,#1fc2c0 60%,#e9e3d4 78%,#f3ede2 100%)}
.hero-band{left:0;top:580px;width:1200px;height:12px;background:var(--yellow)}
.hero-arrow{top:306px;width:104px;height:104px;border-radius:50%;background:#2a2a2a;display:flex;align-items:center}
.hero-arrow.prev{left:-52px;justify-content:flex-end;padding-right:14px}
.hero-arrow.next{left:1148px;justify-content:flex-start;padding-left:14px}

/* feature cards */
.card{top:654px;width:214px;height:394px;background:var(--card-grey)}
.card-head{height:138px;display:flex;justify-content:center;padding-top:20px}
.card-label{position:absolute;left:20px;top:126px;width:174px;height:30px;background:var(--white);text-align:center;font-size:15px;font-weight:600;line-height:30px;text-transform:uppercase}
.card-text{position:absolute;left:26px;top:186px;width:166px;font-family:"Open Sans",sans-serif;font-size:13px;line-height:19px;color:#222}
.card-btn{position:absolute;left:24px;top:348px;width:168px;height:38px;border-radius:19px;color:var(--white);font-weight:300;font-size:19px;text-align:center;line-height:38px}
.card.home .card-head{background:var(--red)} .card.home .card-label{color:var(--red)} .card.home .card-btn{background:linear-gradient(#f0413a,#c9140f)}
.card.area .card-head{background:var(--amber)} .card.area .card-label{color:var(--amber)} .card.area .card-btn{background:linear-gradient(#f2b836,#cf8c05)}
.card.voice .card-head{background:var(--yellow)} .card.voice .card-label{color:var(--amber)} .card.voice .card-btn{background:linear-gradient(#f8d735,#dcae08)}
.card.sights .card-head{background:var(--blue)} .card.sights .card-label{color:var(--blue)} .card.sights .card-btn{background:linear-gradient(#6cc6f2,#2f97d6)}

/* booking */
.booking{left:0;top:1126px;width:1200px;height:744px;background:linear-gradient(180deg,var(--yellow-light),var(--yellow-deep))}
.tag{height:38px;padding:0 26px;border-radius:19px;background:var(--white);color:var(--amber);font-weight:600;font-size:16px;line-height:38px;text-transform:uppercase}
.selector{height:36px;border-radius:18px;background:var(--white);display:flex;align-items:center;justify-content:space-between;padding:0 12px;color:var(--amber);font-size:17px}
.month{width:416px}
.month-title{height:48px;background:var(--white);color:var(--yellow);text-align:center;font-size:28px;font-weight:300;line-height:48px}
.weekdays{display:grid;grid-template-columns:repeat(7,56px);gap:4px;margin-top:6px;height:36px;color:var(--white);font-size:24px;text-align:center;line-height:36px}
.days{display:grid;grid-template-columns:repeat(7,56px);grid-auto-rows:54px;gap:4px;margin-top:10px}
.days span{font-size:22px;font-weight:300;color:var(--yellow);text-align:right;padding:4px 6px 0 0}
.days .d{background:var(--white)}
.days .p{background:var(--pale);color:#f3c238}
.days .b{border:4px solid var(--white)}
.price{height:38px;width:416px;border:4px solid var(--white);border-radius:19px;color:var(--white);font-weight:700;font-size:19px;line-height:30px;padding-left:26px}
.legend{display:flex;align-items:center;gap:24px;color:var(--white);font-weight:600;font-size:18px;line-height:20px}
.swatch{width:50px;height:50px}
.swatch.d{background:var(--white)} .swatch.p{background:var(--pale)} .swatch.b{border:4px solid var(--white)}
.book-now{left:888px;top:1796px;width:160px;height:38px;border-radius:19px;background:linear-gradient(#fff,#ececec);color:var(--yellow);font-size:20px;font-weight:300;text-align:center;line-height:38px}

/* section headings */
.section-head{left:98px;display:flex;align-items:center;width:1032px}
.section-head .tag{background:var(--yellow);color:var(--white);margin-left:26px}
.section-head .rule{flex:1;height:2px;background:var(--line);margin-left:24px}

/* videos */
.video-main{left:100px;top:1986px;width:628px;height:388px;background:linear-gradient(180deg,#3a88d0 0%,#a9d2f0 35%,#34c4c0 55%,#e5dccb 75%,#efe8da 100%)}
.play{left:328px;top:2104px;width:150px;height:150px;border-radius:50%;background:rgba(30,28,22,.85);display:flex;align-items:center;justify-content:center}
.video-item{left:738px;width:392px;display:flex;gap:20px;padding:8px}
.video-item.active{background:var(--amber)}
.thumb{width:180px;height:118px;flex:none;background:linear-gradient(180deg,#3f8ad2,#9fd0ef 40%,#38c6c2 58%,#eae2d2 80%)}
.video-text{font-family:"Open Sans",sans-serif;font-size:15px;line-height:22px;color:var(--amber)}
.video-text b{display:block}
.video-item.active .video-text{color:var(--white)}

/* gallery */
.gallery{left:100px;top:2516px;display:grid;grid-template-columns:repeat(6,158px);grid-auto-rows:158px;gap:22px 16px}
.photo.villa{background:linear-gradient(180deg,#4b8fd6,#d8c39b 45%,#b89968 80%,#8f7d5a)}
.photo.beach{background:linear-gradient(180deg,#3d88d0,#a4d1ef 40%,#36c5c1 58%,#ebe3d3 80%)}

/* footer */
.footer{left:100px;top:2896px;width:1030px;height:100px;background:var(--dark);padding:14px 22px;color:var(--white);font-family:"Open Sans",sans-serif;font-size:12px;line-height:16px}
</style>
</head>
<body>
<div class="abs top-rule"></div>

<header>
  <div class="abs brand">
    <span class="brand-dot"></span>
    <span class="brand-name">CORAL WIND STAYS</span>
  </div>
  <nav class="abs main-nav">
    <span class="nav-pill">THE HOME</span>
    <span class="nav-pill">BOOKING</span>
    <span class="nav-pill">CONTACT US</span>
    <span class="social" aria-label="Social link"></span>
    <span class="social" aria-label="Social link"></span>
  </nav>
</header>

<section>
  <div class="abs hero" role="img" aria-label="Photo slideshow of a white sand Caribbean beach with turquoise sea and palm trees"></div>
  <div class="abs hero-band"></div>
  <div class="abs hero-arrow prev"><svg width="24" height="40" viewBox="0 0 24 40"><path d="M20 4 6 20l14 16" fill="none" stroke="#fff" stroke-width="5"/></svg></div>
  <div class="abs hero-arrow next"><svg width="24" height="40" viewBox="0 0 24 40"><path d="M4 4l14 16L4 36" fill="none" stroke="#fff" stroke-width="5"/></svg></div>
</section>

<section class="features">
  <article class="abs card home" style="left:98px">
    <div class="card-head"><svg width="70" height="70" viewBox="0 0 70 70"><circle cx="35" cy="35" r="34" fill="#fff"/><path d="M16 34 35 18l19 16v18H16z" fill="#e8251f"/><rect x="29" y="36" width="12" height="16" fill="#fff"/></svg></div>
    <div class="card-label">The Home</div>
    <p class="card-text">Lorem ipsum dolor sit amet, consectetuer adipiscing elit. Donec ut purus. Suspendisse venenatis. Quisque vehicula porttitor odio. Quisque arcu ante,</p>
    <div class="card-btn">read more...</div>
  </article>
  <article class="abs card area" style="left:370px">
    <div class="card-head"><svg width="76" height="60" viewBox="0 0 76 60"><path d="M4 16l20-8 20 10 28-10v34L44 52 24 42 4 50z" fill="#fff"/><circle cx="30" cy="14" r="8" fill="#eca80e"/></svg></div>
    <div class="card-label">Local Area</div>
    <p class="card-text">Lorem ipsum dolor sit amet, consectetuer adipiscing elit. Donec ut purus. Suspendisse venenatis. Quisque vehicula porttitor odio. Quisque arcu ante,</p>
    <div class="card-btn">read more...</div>
  </article>
  <article class="abs card voice" style="left:642px">
    <div class="card-head"><svg width="96" height="90" viewBox="0 0 96 90"><ellipse cx="48" cy="40" rx="46" ry="38" fill="#fff"/><path d="M30 72l-8 16 22-12z" fill="#fff"/><path d="M34 40h8v20h-8zM44 40l8-16c4 0 6 3 5 8l-2 6h10c3 0 5 3 4 6l-4 14c-1 2-3 3-5 3H44z" fill="#f3cf1a"/></svg></div>
    <div class="card-label">Testimonials</div>
    <p class="card-text">Lorem ipsum dolor sit amet, consectetuer adipiscing elit. Donec ut purus. Suspendisse venenatis. Quisque vehicula porttitor odio. Quisque arcu ante,</p>
    <div class="card-btn">read more...</div>
  </article>
  <article class="abs card sights" style="left:914px">
    <div class="card-head"><svg width="84" height="84" viewBox="0 0 84 84"><path d="M42 4l10 28 30 2-24 18 9 30-25-18-25 18 9-30L2 34l30-2z" fill="#fff"/></svg></div>
    <div class="card-label">Top Attractions</div>
    <p class="card-text">Lorem ipsum dolor sit amet, consectetuer adipiscing elit. Donec ut purus. Suspendisse venenatis. Quisque vehicula porttitor odio. Quisque arcu ante,</p>
    <div class="card-btn">read more...</div>
  </article>
</section>

<section class="abs booking">
  <svg class="abs" style="left:96px;top:22px" width="44" height="48" viewBox="0 0 44 48"><rect x="2" y="6" width="40" height="40" rx="4" fill="none" stroke="#fff" stroke-width="3"/><rect x="2" y="6" width="40" height="10" fill="#fff"/><g fill="#fff"><rect x="8" y="21" width="6" height="5"/><rect x="19" y="21" width="6" height="5"/><rect x="30" y="21" width="6" height="5"/><rect x="8" y="31" width="6" height="5"/><rect x="19" y="31" width="6" height="5"/><rect x="30" y="31" width="6" height="5"/></g></svg>
  <div class="abs tag" style="left:180px;top:34px">Booking</div>

  <div class="abs selector" style="left:180px;top:94px;width:416px">
    <svg width="14" height="22" viewBox="0 0 14 22"><path d="M11 2 3 11l8 9" fill="none" stroke="#efa80b" stroke-width="3"/></svg>
    <span>AUGUST - SEPTEMBER</span>
    <svg width="14" height="22" viewBox="0 0 14 22"><path d="M3 2l8 9-8 9" fill="none" stroke="#efa80b" stroke-width="3"/></svg>
  </div>
  <div class="abs selector" style="left:640px;top:94px;width:152px">
    <svg width="14" height="22" viewBox="0 0 14 22"><path d="M11 2 3 11l8 9" fill="none" stroke="#efa80b" stroke-width="3"/></svg>
    <span>2014</span>
    <svg width="14" height="22" viewBox="0 0 14 22"><path d="M3 2l8 9-8 9" fill="none" stroke="#efa80b" stroke-width="3"/></svg>
  </div>

  <div class="abs month" style="left:180px;top:156px">
    <div class="month-title">august</div>
    <div class="weekdays"><span>Mo</span><span>Tu</span><span>We</span><span>Th</span><span>Fr</span><span>Sa</span><span>Su</span></div>
    <div class="days">
      <span></span><span></span><span></span><span></span><span></span><span class="d">1</span><span class="d">2</span>
      <span class="d">3</span><span class="d">4</span><span class="p">5</span><span class="p">6</span><span class="p">7</span><span class="p">8</span><span class="p">9</span>
      <span class="d">10</span><span class="d">11</span><span class="d">12</span><span class="d">13</span><span class="d">14</span><span class="d">15</span><span class="d">16</span>
      <span class="d">17</span><span class="d">18</span><span class="d">19</span><span class="d">20</span><span class="d">21</span><span class="d">22</span><span class="d">23</span>
      <span class="d">24</span><span class="d">25</span><span class="d">26</span><span class="d">27</span><span class="d">28</span><span></span><span></span>
    </div>
  </div>

  <div class="abs month" style="left:638px;top:156px">
    <div class="month-title">september</div>
    <div class="weekdays"><span>Mo</span><span>Tu</span><span>We</span><span>Th</span><span>Fr</span><span>Sa</span><span>Su</span></div>
    <div class="days">
      <span></span><span></span><span></span><span></span><span></span><span class="d">1</span><span class="d">2</span>
      <span class="d">3</span><span class="d">4</span><span class="d">5</span><span class="d">6</span><span class="d">7</span><span class="d">8</span><span class="d">9</span>
      <span class="d">10</span><span class="d">11</span><span class="d">12</span><span class="d">13</span><span class="d">14</span><span class="d">15</span><span class="d">16</span>
      <span class="d">17</span><span class="d">18</span><span class="b"></span><span class="b"></span><span class="b"></span><span class="b"></span><span class="b"></span>
      <span class="b"></span><span class="b"></span><span class="d">26</span><span class="b"></span><span class="b"></span><span class="b"></span><span class="b"></span>
    </div>
  </div>

  <div class="abs price" style="left:180px;top:570px">PRICE PER WEEK: €550</div>
  <div class="abs price" style="left:636px;top:570px">PRICE PER NIGHT: €79</div>

  <div class="abs legend" style="left:180px;top:660px">
    <span class="swatch d"></span><span style="width:110px">AVAILABLE</span>
    <span class="swatch p"></span><span style="width:104px;text-align:center">PROVISIONALLY<br>BOOKED</span>
    <span class="swatch b" style="margin-left:8px"></span><span>BOOKED</span>
  </div>
</section>
<div class="abs book-now">book now...</div>

<section>
  <div class="abs section-head" style="top:1922px">
    <svg width="58" height="40" viewBox="0 0 58 40"><rect x="2" y="10" width="36" height="24" rx="4" fill="none" stroke="#f5c518" stroke-width="3"/><path d="M38 16l16-8v24l-16-8z" fill="#f5c518"/><circle cx="46" cy="8" r="6" fill="none" stroke="#f5c518" stroke-width="3"/></svg>
    <span class="tag">Our Videos</span>
    <span class="rule"></span>
  </div>
  <div class="abs video-main" role="img" aria-label="Video still of a tropical beach with leaning palm trees and birds over the sea"></div>
  <div class="abs play"><svg width="70" height="80" viewBox="0 0 70 80"><path d="M8 4l58 36L8 76z" fill="#fff"/></svg></div>

  <div class="abs video-item active" style="top:1986px">
    <div class="thumb" role="img" aria-label="Beach video thumbnail"></div>
    <p class="video-text"><b>Lorem ipsum dolor</b> sit amet, consectetuer adipiscing elit. Donec ut purus. Suspendisse venenatis. Quisque</p>
  </div>
  <div class="abs video-item" style="top:2126px">
    <div class="thumb" role="img" aria-label="Beach video thumbnail"></div>
    <p class="video-text"><b>Lorem ipsum dolor</b> sit amet, consectetuer adipiscing elit. Donec ut purus. Suspendisse venenatis. Quisque</p>
  </div>
  <div class="abs video-item" style="top:2250px">
    <div class="thumb" role="img" aria-label="Beach video thumbnail"></div>
    <p class="video-text"><b>Lorem ipsum dolor</b> sit amet, consectetuer adipiscing elit. Donec ut purus. Suspendisse venenatis. Quisque</p>
  </div>
</section>

<section>
  <div class="abs section-head" style="top:2452px">
    <svg width="58" height="42" viewBox="0 0 58 42"><rect x="2" y="8" width="54" height="32" rx="4" fill="#f5c518"/><rect x="8" y="3" width="12" height="6" fill="#f5c518"/><circle cx="36" cy="22" r="10" fill="none" stroke="#fff" stroke-width="3"/></svg>
    <span class="tag">Gallery</span>
    <span class="rule"></span>
  </div>
  <div class="abs gallery">
    <div class="photo villa" role="img" aria-label="Villa exterior"></div>
    <div class="photo beach" role="img" aria-label="Beach with palm trees"></div>
    <div class="photo beach" role="img" aria-label="Beach with palm trees"></div>
    <div class="photo villa" role="img" aria-label="Villa exterior"></div>
    <div class="photo beach" role="img" aria-label="Beach with palm trees"></div>
    <div class="photo beach" role="img" aria-label="Beach with palm trees"></div>
    <div class="photo beach" role="img" aria-label="Beach with palm trees"></div>
    <div class="photo villa" role="img" aria-label="Villa exterior"></div>
    <div class="photo beach" role="img" aria-label="Beach with palm trees"></div>
    <div class="photo beach" role="img" aria-label="Beach with palm trees"></div>
    <div class="photo villa" role="img" aria-label="Villa exterior"></div>
    <div class="photo beach" role="img" aria-label="Beach with palm trees"></div>
  </div>
</section>

<footer class="abs footer">
  <p>Coral Wind Stays offers a private beach villa on the west coast with sea views, a pool and daily care. Book with confidence through our secure calendar and speak to us directly about dates, transfers, and local tips for your stay.</p>
</footer>
</body>
</html>
```